Welcome to the neighborhood

We need two post card designs for Marsh and Fern Insurance Company.

The first one is when someone moves into a new home.
We want it to include the following:

Congratulations and welcome to the neighborhood.
We are a local independent insurance agency established in 1912
Please let us know if we can be of service to you.

Second post card to send after 6 months in the area should include the following:

Just to let you know................

Marsh and Fern Insurance Agency was established over 100 years ago.
We are in the neighborhood and would appreciate the opportunity to provide you with a no obligation insurance review.
We will offer multiple quotes from several A rated insurance companies and will give you a $10.00 Brewlark gift card to quote your home and auto insurance.
We have saved hundreds of dollars for our clients by offering more coverage at a lower premium.
Please let our professional staff help you with your insurance needs.

Target Market(s)

Individuals that own a home and cars

Industry/Entity Type

Insurance

Font styles to use
Serif

Requirements
Must have
• Marsh and Fern Logo - we have it on jpg file - we tried to attach it but it doesn't seem like it worked
Our colors are black and gold - please incorporate these colors on the postcard
Website www.marshandfern-example.com
Like us on Nestwork
Agency address and phone number
417 Quillon Avenue Suite 318
Alder Ridge, OR 97999
(555)555-0142
Nice to have
• Some visual appeal relative to the topic - home and car - people - somethinng creative

```html
<!DOCTYPE html>
<html lang="en">
<head>
<meta charset="utf-8">
<title>Marsh and Fern – Welcome Postcard</title>
<link rel="stylesheet" href="https://fonts.googleapis.com/css2?family=Gelasio:ital,wght@0,400;0,600;0,700;1,400&display=swap">
<style>
  :root {
    --black: #000000;
    --white: #ffffff;
    --gold-dark: #8f6a22;
    --gold: #b8913a;
    --gold-light: #f6e68e;
    --photo-sky: #b9d8ee;
    --photo-house: #d8dde2;
    --photo-skin: #e8b99a;
    --photo-denim: #6f8fb4;
    --photo-grass: #7aa04a;
  }
  * { margin: 0; padding: 0; box-sizing: border-box; }
  html, body {
    width: 1200px; height: 1000px; overflow: hidden;
    background: var(--white);
    font-family: "Gelasio", Georgia, serif;
  }
  .postcard {
    position: absolute; left: 169px; top: 143px;
    width: 923px; height: 715px;
    background: var(--white); overflow: hidden;
  }
  .postcard__swoosh { position: absolute; left: 0; top: 0; width: 923px; height: 715px; }
  .brand {
    position: absolute; left: 52px; top: 58px; width: 230px;
    text-align: center; color: var(--gold);
  }
  .brand__name { font-size: 24px; font-weight: 700; line-height: 1.1; letter-spacing: 0.5px; }
  .brand__sub { font-size: 17px; font-weight: 700; margin-top: 6px; }
  .brand__est { font-size: 11px; margin-top: 6px; font-weight: 400; }
  .family-photo {
    position: absolute; left: 311px; top: 255px; width: 612px; height: 314px;
    background:
      radial-gradient(ellipse at 55% 45%, var(--photo-skin) 0%, transparent 28%),
      radial-gradient(ellipse at 70% 75%, var(--photo-denim) 0%, transparent 40%),
      linear-gradient(180deg, var(--photo-sky) 0%, var(--photo-house) 45%, var(--photo-grass) 100%);
    -webkit-mask-image: linear-gradient(90deg, transparent 0%, #000 35%);
            mask-image: linear-gradient(90deg, transparent 0%, #000 35%);
  }
  .headline {
    position: absolute; right: 36px; top: 168px; text-align: right; font-weight: 400;
  }
  .headline__main {
    display: block;
    font-size: 69px; font-style: italic; font-weight: 400; line-height: 1;
    background: linear-gradient(90deg, var(--gold-dark) 0%, var(--gold) 30%, var(--gold-light) 55%, var(--gold) 80%, var(--gold-dark) 100%);
    -webkit-background-clip: text; background-clip: text; color: transparent;
    padding-right: 6px;
  }
  .headline__sub {
    display: block;
    font-size: 30px; font-weight: 600; color: var(--gold-dark);
    margin-top: 2px; margin-right: -6px;
  }
  .intro {
    position: absolute; left: 30px; top: 418px; width: 368px;
    text-align: center; font-style: italic; font-size: 26px; line-height: 35px;
    color: var(--black);
  }
  .service-band {
    position: absolute; left: 0; top: 569px; width: 923px; height: 46px;
    background: var(--black);
    border-top: 5px solid var(--gold); border-bottom: 5px solid var(--gold);
    display: flex; align-items: center; justify-content: center;
  }
  .service-band__text {
    font-size: 22px; font-weight: 700; letter-spacing: 1.4px; text-transform: uppercase;
    background: linear-gradient(90deg, var(--gold-dark), var(--gold) 40%, var(--gold-light) 65%, var(--gold));
    -webkit-background-clip: text; background-clip: text; color: transparent;
  }
  .footer { position: absolute; left: 0; top: 615px; width: 923px; height: 100px; background: var(--black); color: var(--white); font-size: 18px; }
  .footer__online { position: absolute; left: 42px; top: 26px; line-height: 26px; }
  .footer__contact { position: absolute; right: 44px; top: 6px; line-height: 23px; text-align: right; font-style: normal; }
</style>
</head>
<body>
  <main class="postcard">
    <svg class="postcard__swoosh" viewBox="0 0 923 715" aria-hidden="true">
      <defs>
        <linearGradient id="goldArc" x1="0" y1="1" x2="1" y2="0">
          <stop offset="0" stop-color="#8f6a22"/>
          <stop offset="0.35" stop-color="#b8913a"/>
          <stop offset="0.6" stop-color="#f6e68e"/>
          <stop offset="1" stop-color="#a47c30"/>
        </linearGradient>
      </defs>
      <path d="M0 0 H923 V95 C650 78 280 110 0 312 Z" fill="#000"/>
      <path d="M0 338 C260 160 600 86 923 96 V101 C600 98 290 175 0 432 Z" fill="url(#goldArc)"/>
    </svg>

    <header class="brand">
      <div class="brand__name">Marsh and Fern</div>
      <div class="brand__sub">Insurance Agency, Inc.</div>
      <div class="brand__est">— est. 1912 —</div>
    </header>

    <div class="family-photo" role="img" aria-label="Photo of a smiling family of three sitting on the lawn in front of their new house"></div>

    <h1 class="headline">
      <span class="headline__main">Congratulations</span>
      <span class="headline__sub">and welcome to the neighborhood.</span>
    </h1>

    <p class="intro">We are a local independent<br>insurance agency<br>established in 1912</p>

    <div class="service-band">
      <p class="service-band__text">Please let us know if we can be of service to you</p>
    </div>

    <footer class="footer">
      <div class="footer__online">
        <p>www.marshandfern-example.com</p>
        <p>Like us on Nestwork</p>
      </div>
      <address class="footer__contact">
        <p>417 Quillon Avenue Suite 318</p>
        <p>Alder Ridge, OR 97999</p>
        <p>(555)555-0142</p>
      </address>
    </footer>
  </main>
</body>
</html>
```